Realty Group Needs Classy, Contemporary Letterhead Design

We need a letterhead design for a new realty company located in NY, USA. We buy investment properties to rehabilitate and or keep in our rental portfolio.

```html
<!DOCTYPE html>
<html lang="en">
<head>
<meta charset="utf-8">
<title>Meridian Realty Group Letterhead</title>
<link href="https://fonts.googleapis.com/css2?family=Montserrat:wght@400;500;600&family=Figtree:wght@400;500&display=swap" rel="stylesheet">
<style>
  :root {
    --backdrop: #e3e3e3;
    --paper: #ffffff;
    --brand-purple: #4b2883;
    --band-gray: #7b7a79;
    --ink: #2e2e2e;
    --ink-soft: #3a3a3a;
    --on-dark: #ffffff;
    --signature-tone: #d9d9d9;
  }
  * { margin: 0; padding: 0; box-sizing: border-box; }
  html, body { width: 1200px; height: 1143px; overflow: hidden; }
  body { background: var(--backdrop); position: relative; }

  .letterhead {
    position: absolute;
    left: 277px; top: 147px;
    width: 647px; height: 846px;
    background: var(--paper);
  }
  .header-band { position: absolute; left: 0; top: 0; width: 647px; height: 120px; }
  .header-band svg { display: block; }

  .brand {
    position: absolute; left: 40px; top: 0; width: 260px; height: 120px;
    display: flex; flex-direction: column; justify-content: center; align-items: center;
    color: var(--on-dark); font-family: "Montserrat", sans-serif; font-weight: 600;
    text-align: center;
  }
  .brand-name { font-size: 27px; line-height: 30px; letter-spacing: 0.2px; }
  .brand-sub { font-size: 12px; line-height: 16px; letter-spacing: 0.4px; margin-top: 2px; }

  .contact {
    position: absolute; right: 68px; top: 20px;
    text-align: right; color: var(--on-dark);
    font-family: "Montserrat", sans-serif; font-size: 10.5px; line-height: 13px;
  }
  .contact .rule { width: 16px; height: 1.5px; background: var(--on-dark); margin: 7px 0 8px auto; }
  .contact-line { display: flex; justify-content: flex-end; align-items: center; gap: 5px; }
  .contact-line svg { width: 7px; height: 7px; flex: none; }

  .salutation {
    position: absolute; left: 67px; top: 240px;
    font-family: "Montserrat", sans-serif; font-weight: 500; font-size: 12.5px; color: var(--ink);
  }
  .paragraph {
    position: absolute; left: 67px; width: 513px;
    font-family: "Figtree", sans-serif; font-size: 9.6px; line-height: 16.1px;
    color: var(--ink-soft); letter-spacing: -0.2px;
  }
  .paragraph .line {
    display: block; white-space: nowrap;
    text-align: justify; text-align-last: justify;
  }
  .paragraph .line.tight { letter-spacing: -0.45px; }
  .p1 { top: 282px; }
  .p2 { top: 363px; }
  .p3 { top: 508px; }

  .signoff { position: absolute; left: 67px; top: 592px; font-family: "Montserrat", sans-serif; color: var(--ink); }
  .signoff-name { font-size: 13.5px; font-weight: 500; line-height: 16px; }
  .signoff-title { font-size: 9px; line-height: 11px; }

  .signature {
    position: absolute; left: 67px; top: 644px; width: 149px; height: 50px;
    background: linear-gradient(90deg, var(--signature-tone), #efefef);
    border-radius: 2px;
  }
</style>
</head>
<body>
  <main class="letterhead">
    <header class="header-band">
      <svg width="647" height="120" viewBox="0 0 647 120" aria-hidden="true">
        <rect x="0" y="0" width="647" height="120" fill="var(--band-gray)"/>
        <polygon points="286,0 296,0 335,60 296,120 286,120 325,60" fill="var(--paper)"/>
        <polygon points="0,0 286,0 325,60 286,120 0,120" fill="var(--brand-purple)"/>
      </svg>
      <div class="brand">
        <div class="brand-name">Meridian</div>
        <div class="brand-sub">Realty Group, LLC</div>
      </div>
      <div class="contact">
        <div>2210 Harbor Street</div>
        <div>Brooklyn, NY 11201</div>
        <div class="rule"></div>
        <div class="contact-line">+1 212 555-0148
          <svg viewBox="0 0 10 10"><path d="M2 1 L4 1 L5 3.5 L3.8 4.5 Q4.8 6.2 6.5 6.5 L7.5 5.3 L9 6.5 L9 8.5 Q5 9 2.5 6 Q1 4 2 1Z" fill="var(--on-dark)"/></svg>
        </div>
        <div class="contact-line">info@meridianrealtygroupllc.com
          <svg viewBox="0 0 10 10"><rect x="1" y="2" width="8" height="6" fill="none" stroke="var(--on-dark)" stroke-width="1"/><path d="M1 2 L5 5.5 L9 2" fill="none" stroke="var(--on-dark)" stroke-width="1"/></svg>
        </div>
        <div class="contact-line">www.meridianrealtygroupllc.com
          <svg viewBox="0 0 10 10"><circle cx="5" cy="5" r="4" fill="none" stroke="var(--on-dark)" stroke-width="1"/><path d="M1 5 H9 M5 1 Q2.5 5 5 9 M5 1 Q7.5 5 5 9" fill="none" stroke="var(--on-dark)" stroke-width="0.8"/></svg>
        </div>
      </div>
    </header>

    <p class="salutation">Dear sir/Madam,</p>

    <p class="paragraph p1">
      <span class="line">Lorem Ipsum is simply dummy text of the printing and typesetting industry. Lorem Ipsum has been the indus-</span>
      <span class="line">try's standard dummy text ever since the 1500s, when an unknown printer took a galley of type and scrambled</span>
      <span class="line">it to make a type specimen book. It has survived not only five centuries, but also the leap into electronic</span>
      <span class="line">typesetting, remaining essentially unchanged. It was popularised in the 1960s with the release of Letrafix</span>
    </p>

    <p class="paragraph p2">
      <span class="line tight">Contrary to popular belief, Lorem Ipsum is not simply random text. It has roots in a piece of classical Latin litera-</span>
      <span class="line">ture from 45 BC, making it over 2000 years old. Thomas Avery, a Latin professor at Harlow</span>
      <span class="line tight">College in Vermont, looked up one of the more obscure Latin words, consectetur, from a Lorem Ipsum passage,</span>
      <span class="line tight">and going through the cites of the word in classical literature, discovered the undoubtable source. Lorem Ipsum</span>
      <span class="line">comes from sections 1.10.32 and 1.10.33 of "de Finibus Bonorum et Malorum" (The Extremes of Good and Evil)</span>
      <span class="line tight">by Marcus Vale, written in 45 BC. This book is a treatise on the theory of ethics, very popular during the Renaissance.</span>
      <span class="line">The first line of Lorem Ipsum, "Lorem ipsum dolor sit amet..", comes from a line in section 1.10.32.</span>
      <span class="line">typesetting, remaining essentially unchanged. It was popularised in the 1960s with the release of Letrafix</span>
    </p>

    <p class="paragraph p3">
      <span class="line">Lorem Ipsum is simply dummy text of the printing and typesetting industry. Lorem Ipsum has been the indus-</span>
      <span class="line">try's standard dummy text ever since the 1500s, when an unknown printer took a galley of type and scrambled</span>
      <span class="line">it to make a type specimen book. It has survived not only five centuries, but also the leap into electronic</span>
      <span class="line">typesetting, remaining essentially unchanged. It was popularised in the 1960s with the release of Letrafix</span>
    </p>

    <div class="signoff">
      <div class="signoff-name">Daniel R. Hale, Esq.</div>
      <div class="signoff-title">Managing Attorney</div>
    </div>

    <div class="signature" role="img" aria-label="Handwritten signature of the managing attorney"></div>
  </main>
</body>
</html>
```